Design for a 170 ml Dessert Cup (Ice Cream / Fruits / Creams)

About Us
We are a small start-up from Switzerland focused on sustainable to-go and street food packaging products, all made with FSC-certified materials. Our name is: marigold lattice - you will find our logo attached.
Our success is strongly driven by the design of our packaging — we position ourselves as a premium brand, offering unique, creative, and stylish designs that stand out from the competition.

Project Overview
We are launching a new product: a dessert cup (170 ml) that will represent our brand's spirit and values.
The design should be simple, beautiful, fresh, cheerful, modern, sweet, and trendy.
Even though this will be used mainly for ice cream, it should also work for fruits, creams, and other desserts. Therefore, please do not include any literal ice cream visuals (eg scoops, cones, flavors).
In the future, we plan to introduce other cup sizes — so the design should be flexible enough to work across different sizes by changing the color scheme (same design, different colors).
For now, we focus on finding the main design for the 170 ml size (approx. 8 cm diameter x 4 cm height).

goal
Create a fun, stylish, and modern design for our 170 ml dessert cup that stands out on the shelf and connects emotionally with customers. Please use the template of the cup (document attached).
Colors should be bright and lively, but not too strong or harsh.
We also like patterns that repeat themselves, simple but stylish.
Sustainability doesn't need to be the main visual theme — creativity and appeal are more important.
If it fits naturally, you may integrate the word “Marigold” (our brand name), but it's optional and should not dominate the design.

Creative Direction/Design Ideas
• Funky & Trendy: playful typography and modern patterns, simple
• Creative & Unique: abstract or quirky elements inspired by desserts, fruits, or textures
• High-Quality & Foody: evoke a sense of taste and indulgence, without showing ice cream directly
• Modern Aesthetics: clean, balanced layouts with simplicity
• Sweet & Soft: pastel or soft color palettes, light and fresh feeling
• You will find some pictures of designs we like attached
Technical Details
• Cup size: 170 ml (8 cm diameter × 4 cm height)
• Design should be easy to recolor for future cup sizes
• You can find the template in the documents of the project

Key Messages
• Quality • Simple • Craving
• Modern • Soft • Fun

Tone & Emotion
The design should feel happy, fresh, and delightful

Target Market(s)

Wholesale markets and small businesses (restaurants, food trucks, ice cream trucks)

Industry/Entity Type

Food Service , Restaurants

Requirements
Must have
• high quality design, simple but fun and beautiful
Should not have
• not a lot of words or no words

```html
<!DOCTYPE html>
<html lang="en">
<head>
<meta charset="utf-8">
<title>Marigold Lattice – 170 ml Dessert Cup Wraps</title>
<link rel="stylesheet" href="https://fonts.googleapis.com/css2?family=Jost:wght@700&display=swap">
<style>
  :root {
    --canvas: #e7e8e9;
    --cut-line: #ef8a8a;
    --safe-line: #9fd27a;
    --edge: #231f20;
    --marigold: #e6be7e;
    --orchid: #db97c4;
    --aqua: #9dd8d9;
    --label: #ffffff;
  }
  html, body {
    margin: 0;
    padding: 0;
    width: 1200px;
    height: 1200px;
    overflow: hidden;
    background: var(--canvas);
  }
  .sheet {
    display: block;
    width: 1200px;
    height: 1200px;
  }
  .cut-guide {
    fill: none;
    stroke: var(--cut-line);
    stroke-width: 0.8;
    stroke-dasharray: 4 3;
  }
  .safe-guide {
    fill: none;
    stroke: var(--safe-line);
    stroke-width: 0.6;
    stroke-dasharray: 3 3;
    opacity: 0.8;
  }
  .wrap-edge {
    fill: none;
    stroke: var(--edge);
    stroke-width: 0.8;
  }
  .brand-name {
    font-family: 'Jost', sans-serif;
    font-weight: 700;
    font-size: 25px;
    letter-spacing: 2.5px;
    fill: var(--label);
    text-transform: uppercase;
  }
  .wrap--marigold .badge { fill: var(--marigold); }
  .wrap--orchid .badge { fill: var(--orchid); }
  .wrap--aqua .badge { fill: var(--aqua); }
</style>
</head>
<body>
<svg class="sheet" viewBox="0 0 1200 1200" xmlns="http://www.w3.org/2000/svg">
  <defs>
    <linearGradient id="pattern-marigold" x1="0" y1="0" x2="1" y2="0" gradientTransform="rotate(8)">
      <stop offset="0" stop-color="#ec8f6c"/>
      <stop offset="0.1" stop-color="#eea86a"/>
      <stop offset="0.2" stop-color="#ecc86a"/>
      <stop offset="0.3" stop-color="#ec9478"/>
      <stop offset="0.42" stop-color="#e8b078"/>
      <stop offset="0.5" stop-color="#e6be7e"/>
      <stop offset="0.58" stop-color="#ec9a70"/>
      <stop offset="0.7" stop-color="#ecc86a"/>
      <stop offset="0.8" stop-color="#ec8f78"/>
      <stop offset="0.9" stop-color="#eec46a"/>
      <stop offset="1" stop-color="#ec9070"/>
    </linearGradient>
    <linearGradient id="pattern-orchid" x1="0" y1="0" x2="1" y2="0" gradientTransform="rotate(8)">
      <stop offset="0" stop-color="#e8789a"/>
      <stop offset="0.1" stop-color="#e89a94"/>
      <stop offset="0.2" stop-color="#e6b890"/>
      <stop offset="0.3" stop-color="#e67a9a"/>
      <stop offset="0.42" stop-color="#e0a0b4"/>
      <stop offset="0.5" stop-color="#db97c4"/>
      <stop offset="0.58" stop-color="#e6848e"/>
      <stop offset="0.7" stop-color="#e6b890"/>
      <stop offset="0.8" stop-color="#e6789c"/>
      <stop offset="0.9" stop-color="#e4aea0"/>
      <stop offset="1" stop-color="#e6829a"/>
    </linearGradient>
    <linearGradient id="pattern-aqua" x1="0" y1="0" x2="1" y2="0" gradientTransform="rotate(8)">
      <stop offset="0" stop-color="#dc8a8e"/>
      <stop offset="0.1" stop-color="#c8c48e"/>
      <stop offset="0.2" stop-color="#b4c890"/>
      <stop offset="0.3" stop-color="#de8e92"/>
      <stop offset="0.42" stop-color="#b8c2b0"/>
      <stop offset="0.5" stop-color="#9dd8d9"/>
      <stop offset="0.58" stop-color="#de9488"/>
      <stop offset="0.7" stop-color="#c8cc8a"/>
      <stop offset="0.8" stop-color="#dc8c96"/>
      <stop offset="0.9" stop-color="#b0c892"/>
      <stop offset="1" stop-color="#dc8e8e"/>
    </linearGradient>
  </defs>

  <g class="wrap wrap--marigold">
    <rect class="cut-guide" x="17.5" y="188" width="1165" height="235"/>
    <rect x="32" y="202.5" width="1136" height="206" fill="url(#pattern-marigold)" role="img" aria-label="Dense repeating pattern of colourful hand-painted popsicles in pink, red, yellow, green and peach on a marigold ground"/>
    <rect class="safe-guide" x="46" y="217" width="1108" height="177"/>
    <rect class="wrap-edge" x="32" y="202.5" width="1136" height="206"/>
    <circle class="badge" cx="601" cy="304" r="88"/>
    <text class="brand-name" x="601" y="298" text-anchor="middle">Marigold</text>
    <text class="brand-name" x="601" y="328" text-anchor="middle">Lattice</text>
  </g>

  <g class="wrap wrap--orchid">
    <rect class="cut-guide" x="17.5" y="482" width="1165" height="235"/>
    <rect x="32" y="497" width="1136" height="205.5" fill="url(#pattern-orchid)" role="img" aria-label="Dense repeating pattern of colourful hand-painted popsicles in pink, red, yellow, green and peach on an orchid ground"/>
    <rect class="safe-guide" x="46" y="511" width="1108" height="177"/>
    <rect class="wrap-edge" x="32" y="497" width="1136" height="205.5"/>
    <circle class="badge" cx="601" cy="598" r="88"/>
    <text class="brand-name" x="601" y="592" text-anchor="middle">Marigold</text>
    <text class="brand-name" x="601" y="622" text-anchor="middle">Lattice</text>
  </g>

  <g class="wrap wrap--aqua">
    <rect class="cut-guide" x="17.5" y="776" width="1165" height="235"/>
    <rect x="32" y="791" width="1136" height="206" fill="url(#pattern-aqua)" role="img" aria-label="Dense repeating pattern of colourful hand-painted popsicles in pink, red, yellow, green and peach on an aqua ground"/>
    <rect class="safe-guide" x="46" y="805" width="1108" height="177"/>
    <rect class="wrap-edge" x="32" y="791" width="1136" height="206"/>
    <circle class="badge" cx="601" cy="892" r="88"/>
    <text class="brand-name" x="601" y="886" text-anchor="middle">Marigold</text>
    <text class="brand-name" x="601" y="916" text-anchor="middle">Lattice</text>
  </g>
</svg>
</body>
</html>
```